Business Card for Kinesiologist Practitioner

I need a logo and business card designing for a Kinesiologist Practitioner. I would like the card to be double sided. The look and feel of the logo and graphics should depict natural healing and well being. I would like a modern, fresh and contemporary design with a professional style. I have attached some logos and business cards that I liek from other natural health practitioners. I have also attached some logos that I like and a mock up of the business card style. Please however use your own creative input to change any element as you feel appropriate.

I have used the strap line "Quiet Meadow Care" which I would like underneath the logo. For the logo I like natural objects and possibly with 3 elements in the design as the course I have studied follows a "Lumora " healing concept (mind, body, soul). Maybe a tree or flower with 3 elements and a representation or suggestion of the human body somehow. You will see from the logos i have uploaded

Industry/Entity Type

Business

Contact Information for Business Card

Please see the mock up attached.

Font styles to use
Serif
Sans Serif

Colors
faa54b
acd036
fbee3d
85cae6

Requirements
Must have
• Note the colours are just suggested colours. Please us your own creative licence.

```html
<!DOCTYPE html>
<html lang="en">
<head>
<meta charset="utf-8">
<title>Quiet Meadow Care – Business Card</title>
<link rel="stylesheet" href="https://fonts.googleapis.com/css2?family=Questrial&family=Open+Sans:wght@400&display=swap">
<style>
  :root {
    --bg-light: #d9d9d9;
    --bg-dark: #7a7a7a;
    --card-white: #ffffff;
    --card-grey: #ececec;
    --leaf-green: #8cbf3a;
    --green-light: #a6cf5a;
    --green-dark: #7aa833;
    --ink: #3a3a3a;
    --white: #ffffff;
  }
  * { margin: 0; padding: 0; box-sizing: border-box; }
  html, body { width: 1200px; height: 900px; overflow: hidden; }
  body {
    background: radial-gradient(ellipse at 45% 40%, var(--bg-light) 0%, #b5b5b5 55%, var(--bg-dark) 100%);
    position: relative;
    font-family: "Questrial", sans-serif;
  }
  .card {
    position: absolute;
    width: 600px;
    height: 340px;
    border-radius: 18px;
    box-shadow: 0 6px 14px rgba(0,0,0,0.35);
    overflow: hidden;
  }
  .card-front {
    left: 150px;
    top: 110px;
    background: linear-gradient(100deg, var(--card-white) 0%, var(--card-grey) 60%, var(--card-white) 100%);
  }
  .card-back {
    left: 420px;
    top: 460px;
    background: linear-gradient(90deg, var(--green-light) 0%, var(--green-dark) 100%);
  }
  .front-brand {
    position: absolute;
    left: 70px;
    top: 140px;
    display: flex;
    align-items: center;
    gap: 14px;
  }
  .brand-dot {
    width: 26px; height: 26px;
    border-radius: 50%;
    background: var(--leaf-green);
  }
  .brand-name {
    font-family: "Questrial", sans-serif;
    font-size: 32px;
    color: var(--leaf-green);
    letter-spacing: 0.5px;
  }
  .practitioner {
    position: absolute;
    right: 40px;
    top: 34px;
    text-align: right;
  }
  .practitioner-name {
    font-family: "Questrial", sans-serif;
    font-size: 22px;
    color: var(--leaf-green);
    font-weight: 700;
  }
  .practitioner-credentials {
    font-family: "Open Sans", sans-serif;
    font-size: 13px;
    color: var(--ink);
    margin-left: 6px;
  }
  .practitioner-role {
    font-family: "Open Sans", sans-serif;
    font-size: 13px;
    color: var(--ink);
    margin-top: 4px;
  }
  .contact {
    position: absolute;
    right: 40px;
    bottom: 46px;
    text-align: right;
    font-family: "Open Sans", sans-serif;
    font-size: 14px;
    color: var(--ink);
    line-height: 1.9;
  }
  .back-brand {
    position: absolute;
    inset: 0;
    display: flex;
    align-items: center;
    justify-content: center;
    gap: 16px;
  }
  .back-brand .brand-dot { background: var(--white); width: 30px; height: 30px; }
  .back-brand .brand-name { color: var(--white); font-size: 40px; }
</style>
</head>
<body>
  <section class="card card-front">
    <div class="practitioner">
      <div><span class="practitioner-name">Clara Benning</span><span class="practitioner-credentials">Dip, Cert.</span></div>
      <div class="practitioner-role">Kinesiologist</div>
    </div>
    <div class="front-brand">
      <span class="brand-dot"></span>
      <span class="brand-name">Quiet Meadow Care</span>
    </div>
    <div class="contact">
      <div>04 55 0123 45</div>
      <div>clarabenning@mail.com</div>
    </div>
  </section>

  <section class="card card-back">
    <div class="back-brand">
      <span class="brand-dot"></span>
      <span class="brand-name">Quiet Meadow Care</span>
    </div>
  </section>
</body>
</html>
```